Redesign of Smart Watch Gift Voucher-SEE ATTACHED CURRENT DESIGN

I need to redesign my existing design using all same content and elements.

MY ENVISION: I invision more of a professional advertisement type of flyer/voucher. Imagine how Corvel.com would create a professionally looking flyer promoting the lumo or veno.

you can get many ideas about professional design by looking at some of corvels flyer designs :
https://www.findora-example.net/search?q=lumo+advertisment&mode=img&ref=a83kd02mzq7

stock photos are attached, you do not have to use them all, you can use some or none i am open to your designs using your own images if you want...just make sure the smartwatch looks black

DO NOT LEAVE ANY CONTENT OR ELEMENTS OUT ON MOCK UP PLEASE

SEE ATTACHED CURRENT DESIGN

I need to redesign my existing design using all same content and elements. DO NOT LEAVE ANY CONTENT OR ELEMENTS OUT ON MOCK UP PLEASE

Target Market(s)

B2B-you can get many ideas about professional design by looking at some of corvels flyer designs :

Industry/Entity Type

Marketing

Requirements
Must have
• I need to redesign my existing design using all same content and elements. DO NOT LEAVE ANY CONTENT OR ELEMENTS OUT ON MOCK UP PLEASE

Nice to have

Should not have

```html
<!DOCTYPE html>
<html lang="en">
<head>
<meta charset="utf-8">
<title>Smart Fitness Watch Reward Voucher</title>
<link href="https://fonts.googleapis.com/css2?family=Montserrat:wght@500;600;700;800;900&family=Lato:wght@400;700&display=swap" rel="stylesheet">
<style>
  :root{
    --blue:#1f63b5;
    --red:#e5252a;
    --ink:#222;
    --slate:#454545;
    --band:#575757;
    --paper:#f6f7f8;
    --white:#fff;
  }
  *{box-sizing:border-box;margin:0;padding:0}
  html,body{width:970px;height:1200px;overflow:hidden}
  body{background:#fff;font-family:"Lato",sans-serif;color:var(--ink)}
  .flyer{position:relative;width:970px;height:1200px;overflow:hidden;
    background:linear-gradient(180deg,#f3f4f5 0%,#fbfbfc 50%,#eef0f2 100%)}
  .hero-photo{position:absolute;left:440px;top:0;width:530px;height:370px;
    background:linear-gradient(135deg,#dcdad4 0%,#c9c6bf 45%,#2f6bc0 46%,#2a5fae 60%,#d7d4cd 61%,#bdb9b2 100%)}
  .headline{position:absolute;left:58px;top:82px;font-family:"Montserrat",sans-serif}
  .headline .enjoy{font-weight:900;font-size:92px;line-height:.9;color:var(--blue);letter-spacing:1px}
  .headline .sub{font-weight:800;font-size:35px;color:var(--slate);margin-top:8px;line-height:1}
  .headline .product{font-weight:900;font-size:46px;color:var(--blue);line-height:1.05}
  .tagline{position:absolute;left:0;top:294px;width:465px;height:76px;background:var(--band);
    color:var(--white);font-family:"Montserrat",sans-serif;font-weight:600;font-size:20.5px;
    line-height:26px;padding:13px 0 0 58px}
  .intro{position:absolute;left:0;top:370px;width:970px;height:146px;background:var(--blue);
    color:var(--white);font-family:"Montserrat",sans-serif;font-weight:500;font-size:15.6px;
    line-height:20px;text-align:center;padding:10px 70px 0}
  .gallery{position:absolute;top:487px;left:20px;display:flex;gap:10px}
  .gallery .shot{width:304px;height:185px;border:4px solid var(--white);box-shadow:0 1px 3px rgba(0,0,0,.15)}
  .shot.desk{background:linear-gradient(135deg,#8a9098,#c8ccd1 55%,#5d6169)}
  .shot.stretch{background:linear-gradient(180deg,#cfcfcf,#bdbdbd)}
  .shot.wrist{background:linear-gradient(135deg,#3c4654,#c49c8a 55%,#2c3440)}
  .tab{position:absolute;top:701px;height:31px;font-family:"Montserrat",sans-serif;font-weight:800;
    font-size:17px;color:var(--white);line-height:31px}
  .tab.features{left:0;width:276px;background:var(--red);border-radius:0 16px 16px 0;padding-left:72px}
  .tab.how{left:334px;width:304px;background:#3d3d3d;border-radius:16px;text-align:center}
  .tab.reviews{left:694px;width:276px;background:var(--red);border-radius:16px 0 0 16px;text-align:center}
  .feature-list{position:absolute;left:72px;top:742px;list-style:none;font-size:17.5px;line-height:22.6px;color:#2a2a2a}
  .feature-list li::before{content:"";display:inline-block;width:5px;height:5px;border-radius:50%;
    background:#2a2a2a;margin:0 12px 4px 0;vertical-align:middle}
  .how-text{position:absolute;left:333px;top:741px;width:315px;font-size:17.5px;line-height:22.6px;color:#2a2a2a}
  .quote{position:absolute;left:695px;top:752px;width:260px;text-align:center;font-size:17.5px;line-height:22.6px;color:#2a2a2a}
  .quote .author{margin-top:23px}
  .quote-mark{position:absolute;font-family:"Montserrat",sans-serif;font-weight:900;font-size:150px;color:#c8c8c8;line-height:1}
  .quote-mark.open{left:688px;top:738px}
  .quote-mark.close{left:862px;top:895px}
  .voucher{position:absolute;left:56px;top:1025px;width:859px;height:141px;border:2px dashed #222;display:flex}
  .voucher .ids{width:212px;border-right:2px dashed #222;margin:22px 0 10px;text-align:center;
    font-family:"Montserrat",sans-serif;font-size:17px;font-weight:500}
  .ids .value{color:var(--red);font-weight:700}
  .ids hr{border:0;border-top:2px dashed #222;width:150px;margin:6px auto 8px}
  .voucher .redeem{flex:1;text-align:center;font-family:"Montserrat",sans-serif;padding-top:16px}
  .redeem .lead{font-weight:700;font-size:19.5px;line-height:24px}
  .redeem .url{font-weight:900;font-size:28px;margin-top:6px;letter-spacing:.3px}
  .redeem .terms{font-weight:600;font-size:15px;margin-top:4px}
</style>
</head>
<body>
<main class="flyer">
  <div class="hero-photo" role="img" aria-label="Runner sitting on stairs checking a black smartwatch and phone, with fitness icons around"></div>
  <header class="headline">
    <div class="enjoy">ENJOY</div>
    <div class="sub">YOUR BRAND NEW</div>
    <div class="product">SMARTWATCH</div>
  </header>
  <div class="tagline">TAKE CONTROL OF YOUR LIFE WITH<br>YOUR NEW SMART FITNESS WATCH</div>
  <p class="intro">Congratulations, you have been rewarded with a Brand New Smart Fitness Watch shipped right to your door. Just pay shipping and handling. Your new Smart Fitness Watch has these features: sport mode, pedometer, distance, calorie, heart rate, blood pressure, stopwatch, sleep monitoring, phone locator, reminders, remote camera, an alarm clock and much more!</p>
  <div class="gallery">
    <div class="shot desk" role="img" aria-label="Hand with smartwatch on a computer mouse beside a keyboard"></div>
    <div class="shot stretch" role="img" aria-label="Woman stretching her arms wearing a black smartwatch"></div>
    <div class="shot wrist" role="img" aria-label="Close-up of a wrist with a black smartwatch showing heart rate"></div>
  </div>
  <div class="tab features">FEATURES</div>
  <div class="tab how">HOW CAN WE DO THIS?</div>
  <div class="tab reviews">WHATS OTHERS SAY</div>
  <ul class="feature-list">
    <li>Pedometer</li><li>Calorie Counter</li><li>Blood Pressure Monitor</li><li>Sleep Monitoring</li>
    <li>Reminders Feature</li><li>Alarm Clock</li><li>Distance Tracker</li><li>Heart Rate Monitor</li>
    <li>Stopwatch</li><li>Phone Locator</li><li>Remote Camera</li><li>Waterproofv</li>
  </ul>
  <p class="how-text">We have a couple retail partners that we team up with to "crowd purchase" huge shipping containers that hold 10's of thousands of electronic products at 80-90% off retail. We simply pass our savings on to you as we do not profit from our electronic products. You are basically able to "piggy back" on our partnerships and buying power to get an attractive electronic premium for a fraction of the retail cost.</p>
  <div class="quote-mark open">“</div>
  <div class="quote-mark close">”</div>
  <blockquote class="quote">
    <p>Are you sure this is<br>not a Norvane<br>Orbit Smartwatch<br>in DISGUISE????<br>I love mine.</p>
    <p class="author">Mason T. Bayview<br>City, NJ</p>
  </blockquote>
  <section class="voucher">
    <div class="ids">
      <div>Certificate ID</div>
      <div class="value">91772-89218</div>
      <hr>
      <div>Expires</div>
      <div class="value">10/03/2020</div>
    </div>
    <div class="redeem">
      <div class="lead">VIEW ALL THE DETAILS OF THIS SPECIAL OFFER<br>AND REDEEM ONLINE AT</div>
      <div class="url">WWW.PERKSANDPRIZEHUB.COM</div>
      <div class="terms">*Terms and Conditions apply see website for details</div>
    </div>
  </section>
</main>
</body>
</html>
```